Fr. K Winery Wine Label Design

We are looking to redesign our wine labels. i have updated this contest to focus on just the premium wines. These should have gold writing on a silk screened bottle, or on black traditional label. Red or gold capsule.
Our logo is of a mountain with dated cursive script (see attached). We are hoping to maintain some of that brand identity but with a more premium look. The current cursive script definitely needs to be altered. Fennick K is an extinct volcano that is a local landmark in the Okanagan Valley. One concept was using this image as a background or element of the labels or a new logo. i have attached an actual photo of the mountain. This is only to inspire a simplified logo.

Target Market(s)

30-65

Logo Text

Fr. (or Fennick) Larrowet

Font styles to use
Serif
Script

Colors
1b1b1b
ec1f27
fbf289

Requirements
Must have
• High End Feel. silkscreen? gold writing. wine is called "Harbor"
Nice to have
• "estate grown"

```html
<!DOCTYPE html>
<html lang="en">
<head>
<meta charset="utf-8">
<title>Fr. K Winery – Label Concepts</title>
<link rel="stylesheet" href="https://fonts.googleapis.com/css2?family=Cinzel:wght@400;600&family=Cormorant+Garamond:ital,wght@0,500;0,600;1,500&display=swap">
<style>
  :root {
    --canvas: #ffffff;
    --glass-green: #bdbd8b;
    --glass-shine: #d6d6ad;
    --glass-black: #111111;
    --shine-dark: #5a5a5a;
    --capsule: #1b1b1b;
    --capsule-red: #ec1f27;
    --label-black: #161616;
    --label-white: #ffffff;
    --gold: #b8912c;
    --gold-light: #c9a441;
    --ink: #111111;
    --paper-ink: #ffffff;
  }
  html, body {
    margin: 0;
    padding: 0;
    width: 1144px;
    height: 1200px;
    overflow: hidden;
    background: var(--canvas);
  }
  .concept-sheet { display: block; width: 1144px; height: 1200px; }
  .draft-tag { font-family: "Cormorant Garamond", serif; font-size: 11px; fill: var(--ink); }
  .brand-wordmark { font-family: "Cinzel", serif; font-weight: 600; font-size: 46px; fill: var(--ink); letter-spacing: 1px; }
  .label-mark { font-family: "Cinzel", serif; font-weight: 600; font-size: 15px; }
  .label-house { font-family: "Cinzel", serif; font-size: 6.4px; letter-spacing: 1.3px; }
  .label-tagline { font-family: "Cinzel", serif; font-size: 3.6px; letter-spacing: 1.4px; }
  .label-wine { font-family: "Cinzel", serif; font-weight: 600; font-size: 7px; letter-spacing: 1.6px; }
  .label-year { font-family: "Cinzel", serif; font-size: 5.2px; letter-spacing: 1.6px; }
  .label-region { font-family: "Cormorant Garamond", serif; font-style: italic; font-size: 5.6px; }
  .label-cuvee { font-family: "Cormorant Garamond", serif; font-weight: 600; font-size: 8px; }
  .harbor-name { font-family: "Cinzel", serif; font-size: 6.4px; letter-spacing: 2.4px; }
  .fill-white { fill: var(--paper-ink); }
  .fill-gold { fill: var(--gold); }
  .fill-ink { fill: var(--ink); }
</style>
</head>
<body>
<svg class="concept-sheet" viewBox="0 0 629 660" xmlns="http://www.w3.org/2000/svg">
  <defs>
    <path id="bottle-outline" d="M113,182 Q113,175 120,175 L150,175 Q157,175 157,182 L157,268 C157,302 195,310 195,352 L195,616 Q195,626 185,626 L85,626 Q75,626 75,616 L75,352 C75,310 113,302 113,268 Z"/>
    <clipPath id="bottle-clip"><use href="#bottle-outline"/></clipPath>
  </defs>

  <text class="draft-tag" x="140" y="52">DRAFT</text>
  <text class="brand-wordmark" x="315" y="102" text-anchor="middle">Fr. Larrowet</text>

  <!-- Bottle one: black traditional label -->
  <g class="bottle bottle--classic">
    <use href="#bottle-outline" fill="var(--glass-green)"/>
    <g clip-path="url(#bottle-clip)">
      <rect class="capsule" x="100" y="170" width="70" height="86" fill="var(--capsule)"/>
      <rect class="capsule-stripe" x="100" y="253" width="70" height="1" fill="var(--capsule-red)"/>
      <rect class="glass-shine" x="175" y="368" width="9" height="242" fill="var(--glass-shine)"/>
      <rect class="front-label" x="70" y="428" width="130" height="130" fill="var(--label-black)"/>
      <rect x="70" y="547" width="130" height="0.8" fill="var(--capsule-red)"/>
    </g>
    <text class="label-mark fill-white" x="135" y="476" text-anchor="middle">Fr. Larrowet</text>
    <text class="label-house fill-white" x="135" y="494" text-anchor="middle">FENNICK LARROWET</text>
    <text class="label-tagline fill-white" x="135" y="501" text-anchor="middle">FAMILY ESTATE WINERY</text>
    <text class="label-wine fill-gold" x="135" y="527" text-anchor="middle">WINENAME</text>
    <text class="label-year fill-white" x="135" y="537" text-anchor="middle">2017</text>
  </g>

  <!-- Bottle two: white label, gold lettering -->
  <g class="bottle bottle--reserve" transform="translate(160,0)">
    <use href="#bottle-outline" fill="var(--glass-green)"/>
    <g clip-path="url(#bottle-clip)">
      <rect class="capsule" x="100" y="170" width="70" height="86" fill="var(--capsule)"/>
      <rect class="capsule-stripe" x="100" y="254" width="70" height="1" fill="var(--capsule-red)"/>
      <rect class="glass-shine" x="175" y="368" width="9" height="242" fill="var(--glass-shine)"/>
      <rect class="front-label" x="70" y="430" width="130" height="128" fill="var(--label-white)"/>
      <rect x="78" y="438" width="110" height="0.8" fill="var(--gold)"/>
      <rect x="70" y="548" width="130" height="10" fill="var(--gold)"/>
    </g>
    <text class="label-mark fill-gold" x="135" y="476" text-anchor="middle">Fr. Larrowet</text>
    <text class="label-house fill-gold" x="135" y="494" text-anchor="middle">FENNICK LARROWET</text>
    <text class="label-tagline fill-gold" x="135" y="501" text-anchor="middle">FAMILY ESTATE WINERY</text>
    <text class="label-cuvee fill-ink" x="135" y="522" text-anchor="middle">Winemakers Reserve</text>
    <text class="label-region fill-gold" x="135" y="529" text-anchor="middle">Okanagan Valley</text>
    <text class="label-year fill-gold" x="135" y="543" text-anchor="middle">2017</text>
  </g>

  <!-- Bottle three: silkscreened black glass, Harbor -->
  <g class="bottle bottle--harbor" transform="translate(340,0)">
    <use href="#bottle-outline" fill="var(--glass-black)"/>
    <g clip-path="url(#bottle-clip)">
      <rect class="capsule" x="100" y="170" width="70" height="52" fill="var(--capsule)"/>
      <rect class="capsule-stripe" x="100" y="221" width="70" height="0.8" fill="var(--capsule-red)"/>
      <rect class="glass-shine" x="150" y="205" width="4" height="60" fill="var(--shine-dark)"/>
      <rect class="glass-shine" x="178" y="368" width="10" height="240" fill="var(--shine-dark)"/>
    </g>
    <text class="harbor-name fill-gold" x="135" y="334" text-anchor="middle">HARBOR</text>
    <text class="label-mark fill-gold" x="135" y="410" text-anchor="middle" style="font-size:17px">Fr. Larrowet</text>
    <text class="label-house fill-white" x="135" y="548" text-anchor="middle">FENNICK LARROWET</text>
    <text class="label-tagline fill-white" x="135" y="555" text-anchor="middle">FAMILY ESTATE WINERY</text>
    <text class="label-region fill-gold" x="135" y="570" text-anchor="middle">Okanagan Valley</text>
    <text class="label-year fill-gold" x="135" y="584" text-anchor="middle">2017</text>
  </g>
</svg>
</body>
</html>
```